We need a website design for an HVAC (Heating & Air Conditioning) Contractor*

Our HVAC client would like to have a more professional looking site as their current one (https://brisvanecomfortworks.example/) is a template site. We will be building the site in-house from the concept.
Items we'd like to incorporate:
- A banner on the homepage that has a click to call plus a form on the right side of the banner
- There is a video on the current website homepage, please find a place to incorporate this.
- We will need to have at least 800 words of content on the homepage, please find space for that (can be a description of a few of the heating / air conditioning services they do). Feel free to use filler content (lorem ipsum) if need be to just show how the content would look

All submissions must have a homepage and a related subpage concept.

Number of Pages Required

1 page

```html
<!DOCTYPE html>
<html lang="en">
<head>
<meta charset="utf-8">
<title>Brisvane Comfort Works – Heating &amp; Air Conditioning</title>
<link href="https://fonts.googleapis.com/css2?family=Montserrat:wght@400;500;600;700;800&family=Roboto:ital,wght@0,400;0,500;0,700;1,400&display=swap" rel="stylesheet">
<style>
:root{
  --navy:#1c3b69;
  --navy-deep:#16305a;
  --red:#c2231e;
  --red-bright:#d8261f;
  --grey-band:#ecebec;
  --text:#4a4a4a;
  --muted:#6b6b6b;
  --white:#ffffff;
  --footer-bar:#4b4b4d;
}
*{margin:0;padding:0;box-sizing:border-box}
html,body{width:1200px;height:3302px;overflow:hidden}
body{position:relative;font-family:"Roboto",Arial,sans-serif;color:var(--text);background:var(--white)}
.abs{position:absolute}
.accent{color:var(--red)}

/* header */
.site-header{position:absolute;left:0;top:0;width:1200px;height:115px;background:var(--white)}
.brand{position:absolute;display:flex;align-items:center;gap:10px;font-family:"Montserrat",Arial,sans-serif;font-weight:800;color:var(--red);letter-spacing:.5px;white-space:nowrap}
.brand .mark{width:18px;height:18px;background:var(--red)}
.header-brand{left:84px;top:40px;font-size:27px;line-height:30px}
.top-info{position:absolute;top:21px;font-size:12.5px;text-align:left;white-space:nowrap}
.top-info .label{color:var(--red);font-weight:700;font-size:13px;display:flex;align-items:center;gap:5px}
.top-info .value{color:#555;margin-top:4px;padding-left:15px}
.follow-icons{display:flex;gap:3px;margin-top:5px}
.follow-icons span{width:12px;height:12px;background:var(--navy)}
.main-nav{position:absolute;left:445px;top:75px;width:755px;height:40px}
.main-nav svg{position:absolute;left:0;top:0}
.main-nav ul{position:absolute;left:0;top:0;list-style:none;width:100%;height:40px}
.main-nav li{position:absolute;top:12px;color:var(--white);font-family:"Montserrat",Arial,sans-serif;font-weight:700;font-size:14px;white-space:nowrap}

/* hero */
.hero{position:absolute;left:0;top:115px;width:1200px;height:587px;background:linear-gradient(100deg,#3e4249 0%,#5f646c 45%,#7d8289 70%,#5b6068 100%)}
.hero-title{position:absolute;left:117px;top:163px;color:var(--white);font-family:"Montserrat",Arial,sans-serif;font-weight:700;font-size:45px;line-height:48px;white-space:nowrap}
.hero-sub{position:absolute;left:120px;top:272px;color:var(--white);font-family:"Montserrat",Arial,sans-serif;font-size:22px;line-height:29px;font-weight:400;white-space:nowrap}
.review-btn{position:absolute;left:120px;top:382px;width:172px;height:53px;background:#3c7be0;border-radius:3px;display:flex;align-items:center}
.review-btn .badge{width:50px;height:49px;margin-left:2px;background:var(--white);border-radius:2px;flex:none}
.review-btn p{color:var(--white);font-size:11.5px;line-height:13px;margin-left:6px;white-space:nowrap}
.call-btn{position:absolute;left:310px;top:382px;width:171px;height:53px;background:var(--red);border-radius:3px;color:var(--white);font-family:"Montserrat",Arial,sans-serif;font-weight:700;font-size:19px;letter-spacing:1.5px;display:flex;align-items:center;justify-content:center}
.request-panel{position:absolute;left:782px;top:136px;width:299px;height:343px;background:var(--navy)}
.request-panel h2{position:absolute;left:0;top:27px;width:100%;text-align:center;color:var(--white);font-family:"Montserrat",Arial,sans-serif;font-weight:700;font-size:19px}
.request-panel .field{position:absolute;left:27px;width:244px;height:32px;border:2px solid var(--red);color:#dfe5ee;font-size:10px;padding:9px 0 0 14px}
.request-panel .submit{position:absolute;left:27px;top:273px;width:244px;height:42px;background:var(--red);color:var(--white);font-family:"Montserrat",Arial,sans-serif;font-weight:700;font-size:13.5px;display:flex;align-items:center;justify-content:flex-end;padding-right:20px;gap:22px}

/* about */
.about{position:absolute;left:0;top:702px;width:1200px;height:486px;background:var(--white)}
.video-frame{position:absolute;left:165px;top:116px;width:478px;height:269px;background:linear-gradient(160deg,#6a5d52,#3a3531 60%,#2a2a2c)}
.video-frame .tag{position:absolute;left:6px;top:6px;background:#222;color:var(--white);font-size:13px;font-weight:700;padding:3px 7px}
.video-frame .bar{position:absolute;left:28px;right:10px;bottom:15px;height:4px;background:#777}
.video-frame .play{position:absolute;left:10px;bottom:10px}
.section-title{font-family:"Montserrat",Arial,sans-serif;font-weight:700;color:var(--navy)}
.about h2{position:absolute;left:707px;top:108px;font-size:32px}
.arrow{position:absolute}
.about-copy{position:absolute;left:708px;top:185px;width:336px;font-size:13px;line-height:17.2px;text-align:justify;color:#666}
.learn-btn{position:absolute;left:704px;top:356px}
.learn-btn span{position:absolute;left:0;top:0;width:139px;height:35px;display:flex;align-items:center;padding-left:12px;color:var(--white);font-family:"Montserrat",Arial,sans-serif;font-weight:700;font-size:14px;white-space:nowrap}

/* services */
.services{position:absolute;left:0;top:1188px;width:1200px;height:586px;background:var(--grey-band)}
.services h2{position:absolute;left:0;top:78px;width:100%;text-align:center;font-size:32px;font-weight:600}
.service-card{position:absolute;top:192px;width:229px}
.service-card .photo{height:240px}
.service-card .label{height:47px;background:var(--navy);color:var(--white);font-family:"Montserrat",Arial,sans-serif;font-weight:700;font-size:13px;display:flex;align-items:center;justify-content:center;text-align:center;line-height:17px}
.service-card .more{margin-top:16px;text-align:center;color:var(--red);font-size:14px;font-weight:500}

/* contact */
.contact{position:absolute;left:0;top:1774px;width:1200px;height:622px;background:var(--navy)}
.contact h2{position:absolute;color:var(--white);font-family:"Montserrat",Arial,sans-serif;font-weight:700;font-size:28px;white-space:nowrap}
.contact .details{position:absolute;top:156px;color:var(--white);font-size:13.5px;line-height:17px;white-space:nowrap}
.map{position:absolute;left:101px;top:271px;width:523px;height:280px;background:linear-gradient(135deg,#e9e8e4,#dcdcd6);border:2px solid #d0d0d0}
.form-label{position:absolute;left:726px;color:var(--white);font-size:15px}
.form-input{position:absolute;left:726px;width:342px;background:#f4f4f4;border:1px solid #ccc}
.send-btn{position:absolute;left:725px;top:525px;width:124px;height:38px;background:var(--white);color:var(--red);font-family:"Montserrat",Arial,sans-serif;font-weight:700;font-size:14px;display:flex;align-items:center;justify-content:center}

/* reviews */
.reviews{position:absolute;left:0;top:2396px;width:1200px;height:484px;background:var(--white)}
.reviews h2{position:absolute;left:0;top:45px;width:100%;text-align:center;font-size:30px}
.reviews .intro{position:absolute;left:0;top:121px;width:100%;text-align:center;font-size:12px;line-height:16px;color:#555}
.avatar{position:absolute;left:569px;top:178px;width:70px;height:70px;border-radius:50%;background:linear-gradient(160deg,#2e3f5e,#151f33)}
.reviewer{position:absolute;left:0;top:253px;width:100%;text-align:center;font-family:"Montserrat",Arial,sans-serif;font-weight:700;color:var(--navy);font-size:24px}
.stars{position:absolute;left:0;top:289px;width:100%;text-align:center;color:#f39c12;font-size:12px;letter-spacing:2px}
.quote{position:absolute;left:0;top:330px;width:100%;text-align:center;font-style:italic;font-size:12px;line-height:15.5px;color:#555}
.dots{position:absolute;left:562px;top:433px;display:flex;gap:9px}
.dots span{width:7px;height:7px;border-radius:50%;background:#ccc}
.dots span:first-child{background:#999}

/* newsletter */
.newsletter{position:absolute;left:0;top:2880px;width:1200px;height:77px;background:var(--red)}
.newsletter h2{position:absolute;left:256px;top:19px;color:var(--white);font-family:"Roboto",Arial,sans-serif;font-weight:400;font-size:30px;white-space:nowrap}
.newsletter .email{position:absolute;left:577px;top:21px;width:375px;height:34px;background:var(--white);color:#444;font-size:14px;padding:9px 0 0 25px}
.newsletter .subscribe{position:absolute;left:952px;top:21px;width:126px;height:34px;background:var(--navy);color:var(--white);font-size:15px;font-weight:500;display:flex;align-items:center;justify-content:center}

/* footer */
.site-footer{position:absolute;left:0;top:2957px;width:1200px;height:298px;background:var(--navy)}
.footer-brand{left:112px;top:48px;font-size:27px;color:var(--white)}
.footer-brand .mark{background:var(--white)}
.footer-about{position:absolute;left:112px;top:138px;width:265px;color:var(--white);font-size:12px;line-height:15px;text-align:justify}
.footer-social{position:absolute;left:116px;top:223px;display:flex;gap:5px}
.footer-social span{width:19px;height:19px;background:var(--red)}
.footer-col h3{position:absolute;top:54px;color:var(--red);font-family:"Montserrat",Arial,sans-serif;font-weight:600;font-size:13px;white-space:nowrap}
.quick-links{position:absolute;left:458px;top:97px;list-style:none}
.quick-links li{color:var(--white);font-size:12.5px;height:23px;display:flex;gap:12px;white-space:nowrap}
.quick-links li::before{content:"";width:0;height:0;border-left:6px solid var(--red);border-top:4px solid transparent;border-bottom:4px solid transparent;margin-top:3px}
.services-list{position:absolute;left:645px;top:95px;list-style:none}
.services-list li{color:var(--white);font-size:11.5px;line-height:14px;width:158px;height:25.5px;padding-top:5px;border-bottom:1px solid #b8c3d5;white-space:nowrap}
.services-list li:last-child{border-bottom:none;padding-left:4px}
.contact-list{position:absolute;left:871px;top:106px;color:var(--white);font-size:12px;line-height:15px}
.contact-list .row{position:absolute;left:0;display:flex;gap:10px;width:240px;white-space:nowrap}
.copyright{position:absolute;left:0;top:3255px;width:1200px;height:47px;background:var(--footer-bar);color:#ddd;font-size:12px;text-align:center;padding-top:17px}
</style>
</head>
<body>

<header class="site-header">
  <div class="brand header-brand"><span class="mark"></span>BRISVANE</div>
  <div class="top-info" style="left:536px">
    <div class="label"><svg width="10" height="10" viewBox="0 0 10 10"><path d="M2 0 L4 2.5 L3 4 Q4.5 6 6 7 L7.5 6 L10 8 L8.5 10 Q3 9 0 1.5Z" fill="#c2231e"/></svg>Call Us Now</div>
    <div class="value">(555) 014-2870</div>
  </div>
  <div class="top-info" style="left:768px">
    <div class="label"><svg width="11" height="8" viewBox="0 0 11 8"><rect width="11" height="8" fill="#c2231e"/><path d="M0 0 L5.5 4.5 L11 0" stroke="#fff" fill="none"/></svg>Contact Email</div>
    <div class="value">hello@brisvanecomfort.example</div>
  </div>
  <div class="top-info" style="left:1058px;top:18px">
    <div class="label">Follow Us</div>
    <div class="follow-icons"><span></span><span></span><span></span><span></span><span></span></div>
  </div>
  <nav class="main-nav">
    <svg width="755" height="40"><polygon points="26,0 755,0 755,40 0,40" fill="#1c3b69"/></svg>
    <ul>
      <li style="left:57px">HOME</li>
      <li style="left:164px">ABOUT US</li>
      <li style="left:293px">SERVICES</li>
      <li style="left:414px">BLOG</li>
      <li style="left:506px">FAQS</li>
      <li style="left:599px">CONTACT US</li>
    </ul>
  </nav>
</header>

<section class="hero" role="img" aria-label="Technician servicing a wall-mounted air conditioning unit">
  <h1 class="hero-title">KEEP YOUR FRIENDS AND<br>FAMILY COMFORTABLE</h1>
  <p class="hero-sub">WE NOW OFFER A FULL LINE OF SANITATION SERVICES<br>TO COMBAT COVID-19!<br>ASK US ABOUT THESE SERVICES TODAY</p>
  <div class="review-btn"><span class="badge"></span><p>Click here to leave us<br>a review online!</p></div>
  <div class="call-btn">CALL NOW</div>
  <form class="request-panel">
    <h2>SERVICE REQUEST</h2>
    <div class="field" style="top:60px">Name</div>
    <div class="field" style="top:101px">Service</div>
    <div class="field" style="top:141px">Email Address</div>
    <div class="field" style="top:182px">Phone</div>
    <div class="field" style="top:222px">Location</div>
    <div class="submit"><span>SUBMIT</span><span>SUMMIT</span></div>
  </form>
</section>

<section class="about">
  <div class="video-frame" role="img" aria-label="Company video still of a family relaxing at home, with phone number and brisvanecomfortworks.example">
    <span class="tag">IMG_0001</span>
    <svg class="play" width="14" height="14"><polygon points="1,0 14,7 1,14" fill="#fff"/></svg>
    <div class="bar"></div>
  </div>
  <h2 class="section-title">ABOUT <span class="accent">US</span></h2>
  <svg class="arrow" style="left:709px;top:161px" width="63" height="10"><line x1="0" y1="5" x2="56" y2="5" stroke="#c2231e" stroke-width="2"/><polygon points="55,1 63,5 55,9" fill="#c2231e"/></svg>
  <p class="about-copy">Lorem ipsum dolor sit amet, cu per porro dolore nostro, partem integre corpora per ea, tation ornatus mel ad. Brute voluptatibus an est, per cu utroque torquatos, ei eum amet hinc. Ne vix ludus timeam definitionem. His hinc dicunt minimum cu, qui te dico laoreet. Sea ea mucius diceret insolens, eos ei nostrud appellantur, an autem vocent dolorem vel. Ne adhuc accusata eleifend has,</p>
  <div class="learn-btn">
    <svg width="139" height="35"><polygon points="0,0 124,0 139,35 0,35" fill="#1c3b69"/></svg>
    <span>LEARN MORE</span>
  </div>
</section>

<section class="services">
  <h2 class="section-title">Our Main <span class="accent">Services</span></h2>
  <svg class="arrow" style="left:566px;top:140px" width="63" height="10"><line x1="0" y1="5" x2="56" y2="5" stroke="#c2231e" stroke-width="2"/><polygon points="55,1 63,5 55,9" fill="#c2231e"/></svg>
  <article class="service-card" style="left:90px">
    <div class="photo" role="img" aria-label="Worker installing ductwork" style="background:linear-gradient(160deg,#b9b8b2,#7f8a84)"></div>
    <div class="label">GEOTHERMAL</div>
    <div class="more">Learn More →</div>
  </article>
  <article class="service-card" style="left:350px">
    <div class="photo" role="img" aria-label="Refrigerant pressure gauges" style="background:linear-gradient(160deg,#5a6f95,#8a4a3a 60%,#6e6a30)"></div>
    <div class="label">COMMERCIAL HVAC REPAIRS</div>
    <div class="more">Learn More →</div>
  </article>
  <article class="service-card" style="left:613px">
    <div class="photo" role="img" aria-label="Close-up of a condenser fan grille" style="background:linear-gradient(160deg,#4a4d52,#25272b)"></div>
    <div class="label">COMMERCIAL HVAC<br>INSTALLATION</div>
    <div class="more">Learn More →</div>
  </article>
  <article class="service-card" style="left:873px">
    <div class="photo" role="img" aria-label="Outdoor air conditioning condenser unit" style="background:linear-gradient(160deg,#a89a88,#8d939b 55%,#6f6a62)"></div>
    <div class="label">MAINTENANCE PLAN</div>
    <div class="more">Learn More →</div>
  </article>
</section>

<section class="contact">
  <h2 style="left:105px;top:80px">Contact <span class="accent">us</span></h2>
  <svg class="arrow" style="left:106px;top:125px" width="83" height="10"><line x1="0" y1="5" x2="76" y2="5" stroke="#fff" stroke-width="1.5"/><polygon points="75,1 83,5 75,9" fill="#fff"/></svg>
  <div class="details" style="left:105px">Brisvane Comfort Works, LLC<br>418 Fairmont Ave,<br>Ridgeview, OK 73000</div>
  <div class="details" style="left:339px;top:158px">(555) 014-2870<br>hello@brisvanecomfort.example<br>www.brisvanecomfort.example</div>
  <div class="map" role="img" aria-label="Street map showing the company location"></div>

  <h2 style="left:722px;top:83px">Submit <span class="accent">your info</span></h2>
  <svg class="arrow" style="left:726px;top:129px" width="78" height="10"><line x1="0" y1="5" x2="71" y2="5" stroke="#fff" stroke-width="1.5"/><polygon points="70,1 78,5 70,9" fill="#fff"/></svg>
  <div class="form-label" style="top:153px">Name <sup>*</sup></div>
  <div class="form-input" style="top:179px;height:32px"></div>
  <div class="form-label" style="top:224px">Email <sup>*</sup></div>
  <div class="form-input" style="top:250px;height:32px"></div>
  <div class="form-label" style="top:297px">Subject</div>
  <div class="form-input" style="top:323px;height:32px"></div>
  <div class="form-label" style="top:369px">Message</div>
  <div class="form-input" style="top:393px;height:106px;width:344px"></div>
  <div class="send-btn">SEND</div>
</section>

<section class="reviews">
  <h2 class="section-title">Customers <span class="accent">Reviews</span></h2>
  <svg class="arrow" style="left:559px;top:96px" width="86" height="10"><line x1="0" y1="5" x2="79" y2="5" stroke="#c2231e" stroke-width="2"/><polygon points="78,1 86,5 78,9" fill="#c2231e"/></svg>
  <p class="intro">Constructio interrete. Quia nec honesto quic quam honestius nec turpi turpius.<br>Tria genera bonorum; Quid iudicant sensus?</p>
  <svg class="abs" style="left:150px;top:228px" width="30" height="56"><polyline points="28,2 3,28 28,54" fill="none" stroke="#777" stroke-width="2"/></svg>
  <svg class="abs" style="left:1032px;top:228px" width="30" height="56"><polyline points="2,2 27,28 2,54" fill="none" stroke="#777" stroke-width="2"/></svg>
  <div class="avatar" role="img" aria-label="Reviewer portrait"></div>
  <div class="reviewer">Miles Carver</div>
  <div class="stars">★★★★★</div>
  <p class="quote">Constructio interrete. Quia nec honesto quic quam honestius nec turpi turpius. Tria genera bonorum;<br>Quid iudicant sensus? Quae qui non vident, nihil umquam magnum ac cognitione dignum amaverunt.<br>Dicet pro me ipsa virtus nec untur. Paulum, cum regem</p>
  <div class="dots"><span></span><span></span><span></span><span></span><span></span><span></span><span></span></div>
</section>

<section class="newsletter">
  <svg class="abs" style="left:158px;top:12px" width="53" height="53"><circle cx="26.5" cy="26.5" r="24" fill="none" stroke="#fff" stroke-width="2.5"/><rect x="15" y="19" width="23" height="16" rx="2" fill="#fff"/><polyline points="15,20 26.5,29 38,20" fill="none" stroke="#c2231e" stroke-width="1.5"/></svg>
  <h2>News letter Signup</h2>
  <div class="email">Enter Your Email</div>
  <div class="subscribe">SUBSCRIBE</div>
</section>

<footer class="site-footer">
  <div class="brand footer-brand"><span class="mark"></span>BRISVANE</div>
  <p class="footer-about">Lorem ipsum dolor sit amet, cu per porro dolore nostro, partem integre corpora per ea, tation ornatus mel ad. Brute voluptatibus an est, per cu utroque torquatos, ei eum amet hinc.</p>
  <div class="footer-social"><span></span><span></span><span></span><span></span><span></span></div>

  <div class="footer-col"><h3 style="left:458px">QUICK LINK</h3></div>
  <ul class="quick-links">
    <li>HOME</li><li>ABOUT US</li><li>SERVICES</li><li>BLOG</li><li>FAQS</li><li>CONTACT US</li>
  </ul>

  <div class="footer-col"><h3 style="left:645px">WHAT WE DO</h3></div>
  <ul class="services-list">
    <li>HOME RESIDENTIAL</li><li>HVAC INSTALLATION</li><li>RESIDENTIAL HVAC REPAIR</li><li>GEOTHERMAL</li><li>COMMERCIAL HVAC REPAIRS</li><li>COMMERCIAL HVAC REPAIRS</li>
  </ul>

  <div class="footer-col"><h3 style="left:871px">CONTACT INFO</h3></div>
  <div class="contact-list">
    <div class="row" style="top:0"><svg width="10" height="14" viewBox="0 0 10 14"><path d="M5 0 A5 5 0 0 1 10 5 C10 8 5 14 5 14 C5 14 0 8 0 5 A5 5 0 0 1 5 0Z" fill="#c2231e"/><circle cx="5" cy="5" r="2" fill="#1c3b69"/></svg><span>Brisvane Comfort Works, LLC<br>418 Fairmont Ave, Ridgeview,<br>OK 73000</span></div>
    <div class="row" style="top:71px"><svg width="11" height="11" viewBox="0 0 10 10"><path d="M2 0 L4 2.5 L3 4 Q4.5 6 6 7 L7.5 6 L10 8 L8.5 10 Q3 9 0 1.5Z" fill="#c2231e"/></svg><span style="font-weight:700">(555) 014-2870</span></div>
    <div class="row" style="top:101px"><svg width="12" height="9" viewBox="0 0 11 8"><rect width="11" height="8" fill="#c2231e"/><path d="M0 0 L5.5 4.5 L11 0" stroke="#1c3b69" fill="none"/></svg><span>HELLO@BRISVANECOMFORT.EXAMPLE</span></div>
  </div>
</footer>

<div class="copyright">Copyright 2020, Northline Web Studio, All Right Reserved</div>

</body>
</html>
```